KRV Business Card - Courier/Transportation - Needs Double Sided Business Card

I am searching for business cards for my company. Currently I just need cards for the (3) founders.

We are a new courier/transporation company that specializes in the medical/pharmaceutical arena.

As you will see from our logo, our primary colors are green and black. We strive to have an efficient, streamlined service offering. I like traditional looks, but also want to showcase our young, modern feel. I would like our card to be double sided.

Target Market(s)

Pharmacies
Hospitals
Physcian Office
Labs

Industry/Entity Type

Business

```html
<!DOCTYPE html>
<html lang="en">
<head>
<meta charset="utf-8">
<title>KRV Courier – Business Card</title>
<link href="https://fonts.googleapis.com/css2?family=Barlow:wght@400;500;600;700&display=swap" rel="stylesheet">
<style>
  :root {
    --backdrop: #1b1b1b;
    --card-dark: #2b2b2b;
    --card-light: #ffffff;
    --brand-green: #3dfc00;
    --arrow-grey: #d9d9d9;
    --ink: #1e1e1e;
    --ink-soft: #3a3a3a;
    --paper-text: #e9e9e9;
  }
  * { box-sizing: border-box; margin: 0; padding: 0; }
  html, body { width: 1200px; height: 1000px; overflow: hidden; }
  body {
    background: var(--backdrop);
    font-family: "Barlow", Arial, sans-serif;
    display: flex;
    flex-direction: column;
    align-items: center;
    justify-content: center;
    gap: 60px;
  }
  .card {
    position: relative;
    width: 700px;
    height: 400px;
    overflow: hidden;
    box-shadow: 0 10px 30px rgba(0,0,0,.45);
  }
  .card__arrow { position: absolute; inset: 0; width: 700px; height: 400px; }
  .card--front { background: var(--card-light); }
  .card--back { background: var(--card-dark); }

  .brand {
    position: absolute;
    top: 48px; left: 40px;
    display: flex; align-items: center; gap: 10px;
    font-weight: 700; font-size: 30px; letter-spacing: 1px;
    color: var(--ink);
  }
  .brand__dot { width: 16px; height: 16px; background: var(--brand-green); }

  .holder { position: absolute; left: 40px; bottom: 40px; color: var(--ink); }
  .holder__name { font-weight: 700; font-size: 19px; letter-spacing: .5px; }
  .holder__title { font-size: 14px; margin-top: 4px; color: var(--ink-soft); }
  .holder__web { font-size: 15px; letter-spacing: 1.5px; margin-top: 26px; }

  .contact {
    position: absolute; right: 22px; top: 270px;
    text-align: right; color: var(--ink);
    font-size: 12px; line-height: 1.5;
  }
  .contact__row { display: flex; align-items: center; justify-content: flex-end; gap: 5px; font-weight: 600; }
  .contact__badge {
    width: 14px; height: 14px; border-radius: 50%;
    background: var(--brand-green); color: var(--ink);
    font-size: 9px; font-weight: 700;
    display: inline-flex; align-items: center; justify-content: center;
  }
  .contact__address { margin-top: 4px; }

  .back__web {
    position: absolute; top: 30px; left: 36px;
    color: var(--paper-text); font-size: 14px; letter-spacing: 1.5px;
  }
  .back__name {
    position: absolute; left: 270px; top: 250px;
    transform: rotate(-60deg); transform-origin: left center;
    color: var(--paper-text);
    font-weight: 700; font-size: 38px; letter-spacing: 1px;
    white-space: nowrap;
  }
</style>
</head>
<body>

  <section class="card card--front" aria-label="Business card front">
    <svg class="card__arrow" viewBox="0 0 700 400" aria-hidden="true">
      <g transform="translate(380,480) rotate(30)" fill="var(--arrow-grey)">
        <rect x="-55" y="-400" width="110" height="400"/>
        <path fill-rule="evenodd" d="M-210,-400 L0,-640 L210,-400 Z M-125,-440 L0,-580 L125,-440 Z"/>
      </g>
    </svg>
    <div class="brand"><span class="brand__dot"></span>KRV COURIER</div>
    <div class="holder">
      <p class="holder__name">Marcus Lee Hale</p>
      <p class="holder__title">Chief Executive Officer</p>
      <p class="holder__web">www.KRVCourier.net</p>
    </div>
    <div class="contact">
      <p class="contact__row"><span class="contact__badge">M</span>(555) 410-2288</p>
      <p class="contact__row"><span class="contact__badge">E</span>mhale@krvcourier.com</p>
      <p class="contact__address">2450 Alder Creek Dr,<br>Westfield, OH 44001</p>
    </div>
  </section>

  <section class="card card--back" aria-label="Business card back">
    <svg class="card__arrow" viewBox="0 0 700 400" aria-hidden="true">
      <g transform="translate(380,480) rotate(30)" fill="var(--brand-green)">
        <rect x="-55" y="-400" width="110" height="400"/>
        <path fill-rule="evenodd" d="M-210,-400 L0,-640 L210,-400 Z M-125,-440 L0,-580 L125,-440 Z"/>
      </g>
    </svg>
    <p class="back__web">www.KRVCourier.net</p>
    <p class="back__name">KRV COURIER</p>
  </section>

</body>
</html>
```